creation of business cards for Velmora Sàrl

Velmora S% 26 # 224; rl is a soci% 26 # 233; t% 26 # 233; consultancy that accompanies companies in the development of their business on the market% 26 # 233; Switzerland by providing strategic contacts or market information; and by providing administrative or logistical support. Our consulting skills focus on sectors% 26 # 224; high value added% 26 # 233; e, such as trade in food goods% 26 # 39amp; drinks, fashion% 26amp; lifestyle, products and services for% 26 # 233; s in high-tech industries (pharmaceutical, chemical, m% 26 # 233; pricy 26% 23 #; cision) or sustainable solutions (% 26 # 233; energies renewable, mat% 26 # 233; recyclable materials). As part of the launch of our activity% 26 # 233;, we need% 26 # 39;% 26 # 233; to establish business cards to d% 26 # 233; work our new customers (Swiss or international).

Target Market(s)

Companies wishing to develop their activity% 26 # 233; s in Switzerland or% 26 # 224; l% 26 # 39;% 26 # 233; abroad (mainly in Europe).

Contact Information for Business Card

Prénom NOM
Velmora Sàrl
Bureau de Lavertin
Rue des Tilleuls 14, 2000 Neuchâtel
Tél. : 032 718 46 39
info@velmora-conseil.ch
www.velmora-conseil.ch

Font styles to use
Serif
Sans Serif

Colors

Designer to choose colors to be used in the design.

Requirements
Must have
• The logo The name of the company% 26 # 233; t% 26 # 233; (Velmora S% 26 # 224; rl) One field for the mailing address One field for the number% 26 # 233; ro de t% 26 # 233; l% 26 # 233; phone One field for the % 26 # 39; email address and website

```html
<!DOCTYPE html>
<html lang="fr">
<head>
<meta charset="utf-8">
<title>Velmora Sàrl – cartes de visite</title>
<link rel="stylesheet" href="https://fonts.googleapis.com/css2?family=Open+Sans:wght@300;400&display=swap">
<style>
  :root {
    --navy-deep: #042338;
    --navy: #0a3350;
    --teal-navy: #0f4a60;
    --paper: #fbfbfc;
    --ink: #111820;
    --white: #ffffff;
    --backdrop: #e6e8eb;
  }
  * { box-sizing: border-box; margin: 0; padding: 0; }
  html, body {
    width: 1200px; height: 900px; overflow: hidden;
    background: var(--backdrop);
    font-family: "Open Sans", sans-serif;
  }
  .sheet {
    position: relative; width: 1200px; height: 900px;
    display: flex; align-items: center; justify-content: center; gap: 40px;
  }
  .card {
    position: relative; width: 540px; height: 320px;
    border-radius: 4px; overflow: hidden;
    box-shadow: 0 10px 30px rgba(0,0,0,.18);
  }

  /* Front */
  .card-front { background: var(--paper); color: var(--ink); }
  .brand {
    position: absolute; left: 28px; top: 28px;
    display: flex; align-items: center; gap: 18px;
  }
  .brand-square {
    width: 42px; height: 42px; border-radius: 9px; background: var(--navy);
  }
  .brand-name {
    font-weight: 300; font-size: 36px; letter-spacing: 4px;
    color: var(--navy); line-height: 1;
  }
  .address {
    position: absolute; left: 312px; top: 104px;
    display: flex; gap: 10px; font-size: 13px; line-height: 1.35;
  }
  .address svg { width: 12px; height: 17px; flex: none; margin-top: 1px; }
  .band {
    position: absolute; left: 0; right: 0; top: 182px; height: 118px;
    background: linear-gradient(90deg, var(--navy) 0%, var(--navy-deep) 50%, var(--teal-navy) 100%);
    color: var(--white);
  }
  .holder { position: absolute; left: 28px; top: 34px; }
  .holder-name { font-size: 25px; font-weight: 400; line-height: 1.1; letter-spacing: .3px; }
  .holder-company { font-size: 13px; font-weight: 400; letter-spacing: .4px; }
  .contacts {
    position: absolute; left: 318px; top: 18px;
    list-style: none; font-size: 13.5px; line-height: 1;
  }
  .contacts li { display: flex; align-items: center; gap: 12px; height: 27px; }
  .contacts svg { width: 15px; height: 15px; flex: none; }

  /* Back */
  .card-back {
    background: linear-gradient(135deg, var(--navy-deep) 0%, var(--navy) 55%, var(--teal-navy) 100%);
  }
  .back-brand {
    position: absolute; left: 50%; top: 50%; transform: translate(-50%, -50%);
    display: flex; align-items: center; gap: 20px;
  }
  .back-brand .brand-square {
    width: 50px; height: 50px; background: rgba(255,255,255,.06);
  }
  .back-brand .brand-name {
    font-size: 42px; color: rgba(255,255,255,.12);
  }
</style>
</head>
<body>
<main class="sheet">
  <section class="card card-front" aria-label="Recto de la carte">
    <div class="brand">
      <div class="brand-square"></div>
      <div class="brand-name">VELMORA</div>
    </div>

    <div class="address">
      <svg viewBox="0 0 12 17" aria-hidden="true"><path d="M6 0a6 6 0 0 0-6 6c0 4.5 6 11 6 11s6-6.5 6-11a6 6 0 0 0-6-6zm0 8.3A2.3 2.3 0 1 1 6 3.7a2.3 2.3 0 0 1 0 4.6z" fill="#111820"/></svg>
      <p>Bureau de Lavertin<br>Rue des Tilleuls 14,<br>2000 Neuchâtel</p>
    </div>

    <div class="band">
      <div class="holder">
        <p class="holder-name">PRÉNOM NOM</p>
        <p class="holder-company">VELMORA SÀRL</p>
      </div>
      <ul class="contacts">
        <li>
          <svg viewBox="0 0 16 16" aria-hidden="true"><path d="M3.6 1.2l2.2 2.9-1.3 1.6c.9 2 2.5 3.6 4.5 4.6l1.6-1.3 2.9 2.2-1.3 2.5C7 13.6 2.4 9 2.3 3.8z" fill="#fff"/></svg>
          <span>+ 032 718 46 39</span>
        </li>
        <li>
          <svg viewBox="0 0 16 16" aria-hidden="true"><rect x="1" y="3.5" width="14" height="9" fill="#fff"/><path d="M1.5 4l6.5 5 6.5-5" fill="none" stroke="#0a3350" stroke-width="1.2"/></svg>
          <span>info@velmora-conseil.ch</span>
        </li>
        <li>
          <svg viewBox="0 0 16 16" aria-hidden="true"><g fill="none" stroke="#fff" stroke-width="1.1"><circle cx="8" cy="8" r="6.5"/><ellipse cx="8" cy="8" rx="3" ry="6.5"/><path d="M1.5 8h13M2.5 4.8h11M2.5 11.2h11"/></g></svg>
          <span>www.velmora-conseil.ch</span>
        </li>
      </ul>
    </div>
  </section>

  <section class="card card-back" aria-label="Verso de la carte">
    <div class="back-brand">
      <div class="brand-square"></div>
      <div class="brand-name">VELMORA</div>
    </div>
  </section>
</main>
</body>
</html>
```